Create a Brochure Design for Thornbury Homecare

Thornbury Homecare is a subsidiary of the Thornbury Care Group. This brochure is specifically for the Thornbury Homecare company and brand. Create a 3 panel, A4, front and back, tri-fold brochure. This brochure will be a way to introduce our Homecare services to the community, prospective clients, and various referral partners. The brochure must be eye catching, unique in its deliverables and demonstrate both attention to detail and comfort. Our organization is sophisticated and built around warmth, care and individualized personal attention. The most important aspect of this design is to focus on creating a nurturing, warm, and inviting feel where you would want to have a Nurse or Nurse’s Aide in your own home or a loved one’s home.

I am open to the creativity of the designer to develop something based on the above criteria; however I would like the design to work well with the existing collateral material. What I mean by that is that while I want everything to have its own personality and stand out as its own brand representative, I still need to be able to tell that the overall design concept stays stylistically inside of the same ‘family’ of existing designed material. Because of this, below I would like for the designer to pull inspiration from the link to our website (Located below) as well as from the attachment of our recently refreshed business cards (Attached). This should allow each design to be unique and creative, while still staying inside of a framework and the feel/style that I am looking for.

Finally, I want all the designers to understand that this brochure design is for a private, in home, healthcare company where we are responsible for providing personalized care for a culturally and ethnically diverse make-up clientele of all ages. The photos that are used must represent an image of warmth, care, and a positive interaction between client and caregiver.

Look under the Thornbury Homecare tab at www.thornburycaregroup-example.net
Updates

Industry/Entity Type

Healthcare

Requirements
Must have
• • The Thornbury Homecare company logo must be included.

```html
<!DOCTYPE html>
<html lang="en">
<head>
<meta charset="utf-8">
<title>Thornbury Homecare Brochure</title>
<link rel="stylesheet" href="https://fonts.googleapis.com/css2?family=Alegreya:ital,wght@0,400;1,400&family=Mulish:wght@400&display=swap">
<style>
  :root {
    --salmon: #f79a85;
    --teal: #0d6b61;
    --text-grey: #6a6a66;
    --name-grey: #55544f;
    --green-top: #b3c197;
    --green-mid: #f2f4ec;
    --green-bottom: #a9b98a;
  }
  html, body { margin: 0; padding: 0; overflow: hidden; background: #ffffff; }
  .brochure {
    position: relative;
    width: 1200px;
    height: 854px;
    overflow: hidden;
    background: linear-gradient(180deg, var(--green-top) 0%, #d3dbc1 25%, var(--green-mid) 48%, #d6ddc5 66%, var(--green-bottom) 100%);
    font-family: "Mulish", sans-serif;
  }
  .band { position: absolute; background: var(--salmon); }
  .band--top { left: 279px; top: 0; width: 921px; height: 30px; }
  .band--bottom { left: 0; top: 821px; width: 923px; height: 33px; }
  .swirl-lines { position: absolute; inset: 0; pointer-events: none; }

  .founder-portrait {
    position: absolute; left: 36px; top: 39px; width: 146px; height: 182px;
    background: linear-gradient(180deg, #c9868a 0%, #b9646a 45%, #b52a2c 100%);
  }
  .founder-name {
    position: absolute; left: 194px; top: 161px; margin: 0;
    font-family: "Alegreya", serif; font-style: italic; font-weight: 400;
    font-size: 21px; color: var(--name-grey);
  }
  .founder-title {
    position: absolute; left: 194px; top: 189px; margin: 0;
    font-size: 13.5px; line-height: 20px; color: var(--text-grey);
  }
  .story-heading {
    position: absolute; left: 36px; top: 244px; margin: 0;
    font-family: "Alegreya", serif; font-style: italic; font-weight: 400;
    font-size: 21px; color: var(--name-grey);
  }
  .story-body {
    position: absolute; left: 36px; top: 278px; width: 300px;
    font-size: 12.9px; line-height: 19.7px; color: var(--text-grey);
    hyphens: auto;
  }
  .story-body p { margin: 0 0 19.7px; }

  .contact-panel {
    position: absolute; left: 480px; top: 502px; width: 266px; text-align: center;
  }
  .contact-mark {
    width: 30px; height: 30px; margin: 0 auto 6px; background: var(--salmon);
  }
  .contact-name {
    margin: 0; font-family: "Alegreya", serif; font-size: 21px; line-height: 22px;
    color: var(--teal);
  }
  .contact-tagline {
    margin: 3px 0 0; font-family: "Alegreya", serif; font-style: italic;
    font-size: 8.5px; line-height: 9px; color: var(--teal);
  }
  .contact-details {
    margin: 14px 0 0; font-style: normal; font-size: 17px; line-height: 22.4px;
    color: var(--text-grey);
  }

  .cover-mark {
    position: absolute; left: 934px; top: 74px; width: 106px; height: 106px;
    border-radius: 10px; background: var(--salmon);
  }
  .cover-name {
    position: absolute; left: 820px; top: 198px; width: 360px; margin: 0;
    text-align: center; font-family: "Alegreya", serif; font-weight: 400;
    font-size: 56px; line-height: 58px; color: var(--teal);
  }
  .cover-tagline {
    position: absolute; left: 820px; top: 354px; width: 360px; margin: 0;
    text-align: center; font-family: "Alegreya", serif; font-style: italic;
    font-size: 22px; line-height: 23px; color: var(--teal);
  }
  .cover-photo {
    position: absolute; left: 825px; top: 452px; width: 337px; height: 223px;
    background: linear-gradient(110deg, #3a2a28 0%, #5a4240 28%, #c79c94 45%, #d9a98f 62%, #7f8a5c 85%, #6d7a4c 100%);
  }
</style>
</head>
<body>
<main class="brochure">
  <div class="band band--top"></div>
  <div class="band band--bottom"></div>

  <svg class="swirl-lines" width="1200" height="854" viewBox="0 0 1200 854" aria-hidden="true">
    <g fill="none" stroke-width="1.2">
      <path d="M-20 120 C 300 260, 700 60, 1220 40" stroke="#ffffff" opacity="0.55"/>
      <path d="M-20 150 C 320 300, 720 90, 1220 70" stroke="#f3b9a9" opacity="0.5"/>
      <path d="M-20 420 C 300 300, 800 360, 1220 300" stroke="#dfe8f2" opacity="0.6"/>
      <path d="M-20 460 C 340 340, 820 420, 1220 360" stroke="#ffffff" opacity="0.5"/>
      <path d="M-20 780 C 400 640, 800 700, 1220 640" stroke="#e5eef6" opacity="0.6"/>
      <path d="M-20 810 C 420 680, 820 740, 1220 690" stroke="#f3b9a9" opacity="0.45"/>
    </g>
  </svg>

  <div class="founder-portrait" role="img" aria-label="Portrait photo of the founder"></div>
  <h2 class="founder-name">Claire Bennett</h2>
  <p class="founder-title">Founder, President and CEO,<br>Thornbury Care Group</p>

  <h3 class="story-heading">Claire’s Story</h3>
  <div class="story-body">
    <p>Lorem ipsum dolor sit amet, consectetuer adipiscing elit. Nam nibh. Nunc varius facilisis eros. Sed erat. In in velit quis arcu ornare laoreet. Curabitur adipiscing luctus massa. Integer ut purus ac augue commodo commodo. Nunc nec mi eu justo tempor consectetuer. Etiam vitae nisl. In dignissim lacus ut ante. Cras elit lectus, bibendum a, adipiscing vitae, commodo et, dui. Ut tincidunt tortor. Donec nonummy, enim in lacinia pulvinar, velit tellus scelerisque augue, ac posuere libero urna eget neque. Cras ipsum. Vestibulum pretium, lectus nec venenatis volutpat,</p>
    <p>Cras elit lectus, bibendum a, adipiscing vitae, commodo et, dui. Ut tincidunt tortor. Donec nonummy, enim in lacinia pulvinar, velit tellus scelerisque augue, ac posuere libero urna eget neque. Cras ipsum. Vestibulum pretium, lectus nec venenatis volutpat</p>
    <p>Cras elit lectus, bibendum a, adipiscing vitae, commodo et, dui. Ut tincidunt tortor. Donec nonummy, enim in lacinia pulvinar, velit tellus scelerisque augue, ac posuere libero urna eget neque. Cras ipsum. Vestibulum pretium, lectus nec venenatis volutpat</p>
  </div>

  <section class="contact-panel">
    <div class="contact-mark"></div>
    <p class="contact-name">Thornbury Homecare</p>
    <p class="contact-tagline">Care that feels like home...<br>Every single day.</p>
    <address class="contact-details">
      Thornbury Homecare<br>
      480 Maple Harbor Blvd.<br>
      Suite #215<br>
      Lakeview, HI 96800<br>
      T: 555-010-7312<br>
      F: 555-010-7390<br>
      info@thornbury-hc.example
    </address>
  </section>

  <div class="cover-mark"></div>
  <h1 class="cover-name">Thornbury<br>Homecare</h1>
  <p class="cover-tagline">Care that feels like home...<br>Every single day.</p>
  <div class="cover-photo" role="img" aria-label="Photo of a caregiver gently holding an elderly client's hand"></div>
</main>
</body>
</html>
```